Design a cover that embodies the concept of healing by Walking Out of the Fog

Subtitle: How to use tapping, applied kinesiology, and Chinese medicine to heal your body, free your mind and live in peace.

Tapping (Emotional Freedom Technique) is a modern mix of psychology and Chinese medicine that helps people to release the emotions they have inside that are contributing to the depression and anxiety they feel. Applied kinesiology or muscle testing is a biofeedback tool which helps to extract information from the body that can help people to profoundly heal. It can be used to determine whether heavy metals, heavy chemicals, food sensitivities or pathogens are causing the body problems. It can also be used to determine which supplements can help someone heal. This tool also can be used to identify emotions and memories that are also causing someone problems. Lastly, Chinese medicine uses food therapy, herbal formulas, meditation, tai chi (meditative movement), cupping and other tools to help people to be free of depression. This book is written to be information but also details my own personal journey of how I was able to heal from 11 years of heavy depression through the use of these tools.

The heart of the book is about emotional release, emotional freedom and emotional healing. You can surrender, release or let go of emotions and feel better very quickly. This certainly was my experience.

I would like the front and back cover to each be 8.5" x 5.5". I still have to get an ISBN number for the back page as well. Here is the text that I would like on the back cover for now: Millions of people feel the pain, loneliness, and agony of anxiety and depression every day. Many turn to Western medicine in the hopes that a pill will ease the pain and make the problem go away. Oftentimes, this only makes matters worse and doesn’t address the root cause. No one should have to struggle like this when natural answers exist that can address the physical, energetic, emotional, or spiritual causes of anxiety and depression. For 11 long years, Dr. Vance personally struggled with heavy depression until he discovered answers that helped him to completely heal. Walking Out of the Fog is a guide that will help you discover - The two root physical causes of depression and exactly what to do to start healing today - How the negative emotions we have stored within from trauma and bad experiences can drive depression - Tools from Chinese medicine, applied kinesiology, and tapping to help you free your mind and live in peace - An actionable plan to help you let go of the pain, suffering, and negative emotions from your past Whether you feel depressed and anxious or know someone who struggles with these issues, Walking Out of the Fog will transform how you think about depression and will give you the tools to heal so that you can be free and live in peace. Dr. Vance Holbrook is a board-certified acupuncture physician licensed in the state of Florida. He received his training at the Calder Institute of Holistic Practice. He also graduated with a master’s degree in counseling and psychology from Meadowbrook Seminary of Theology. His mission is to help people transform their health and improve the quality of their life naturally. He lives in Orlando, FL where he runs a holistic medical clinic called Bluepine Wellness Center. www.drvanceholbrook-example.com Instagram: drvanceholbrook Facebook: bluepinewellnesscenter

Target Market(s)

Those who suffer from depression and anxiety and want to heal naturally

Industry/Entity Type

Health And Wellness

Requirements
Must have
• My picture should be small and go on the back cover next to the information about me. The front cover would be all graphical. Thank you. On the front cover my name should be posted as "Dr. Vance Holbrook, AP, MA"

```html
<!DOCTYPE html>
<html lang="en">
<head>
<meta charset="utf-8">
<title>Walking Out of the Fog – Cover Spread</title>
<link href="https://fonts.googleapis.com/css2?family=Gochi+Hand&family=Patrick+Hand&family=Tinos&display=swap" rel="stylesheet">
<style>
  :root {
    --page-bg: #ececec;
    --paper: #ffffff;
    --ink: #111111;
    --accent: #e0201b;
    --photo-warm: #c9a887;
    --photo-green: #7d8a5a;
    --art-light: #f2f2f2;
    --art-mid: #bdbdbd;
  }
  * { margin: 0; padding: 0; box-sizing: border-box; }
  html, body { width: 899px; height: 1200px; overflow: hidden; background: var(--page-bg); }
  .canvas { position: relative; width: 899px; height: 1200px; }

  .spread {
    position: absolute; left: 20px; top: 303px;
    width: 860px; height: 594px;
    background: var(--paper);
    box-shadow: 0 2px 8px rgba(0,0,0,.35);
    overflow: hidden;
    color: var(--ink);
  }
  .spread-shapes { position: absolute; inset: 0; width: 100%; height: 100%; }

  /* back cover */
  .back-icon { position: absolute; left: 192px; top: 32px; width: 36px; height: 26px; }
  .back-copy {
    position: absolute; left: 39px; top: 68px; width: 332px;
    font-family: "Patrick Hand", cursive;
    font-size: 8.7px; line-height: 13.2px; letter-spacing: .15px;
    text-align: justify;
  }
  .back-copy p { margin-bottom: 11px; }
  .back-copy .highlight { color: var(--accent); }
  .author-photo {
    position: absolute; left: 39px; top: 383px; width: 101px; height: 97px;
    background: linear-gradient(135deg, var(--photo-green), var(--photo-warm));
  }
  .author-bio {
    position: absolute; left: 156px; top: 381px; width: 226px;
    font-family: "Tinos", serif; font-size: 7.6px; line-height: 10.4px;
    text-align: justify;
  }
  .author-links {
    position: absolute; left: 39px; top: 488px;
    font-family: "Tinos", serif; font-size: 7.4px; line-height: 10.2px;
  }

  /* spine */
  .spine {
    position: absolute; left: 433px; top: 46px; height: 500px; width: 30px;
  }
  .spine-text {
    position: absolute; left: 0; top: 0;
    transform-origin: 0 0; transform: translateX(30px) rotate(90deg);
    white-space: nowrap; font-family: "Gochi Hand", cursive;
    display: flex; align-items: baseline; gap: 46px;
  }
  .spine-title { font-size: 25px; }
  .spine-title .accent { color: var(--accent); text-decoration: underline; text-decoration-thickness: 2px; }
  .spine-author { font-size: 15px; }

  /* front cover */
  .front-title {
    position: absolute; left: 486px; top: 38px; width: 370px;
    font-family: "Gochi Hand", cursive; font-size: 50px; line-height: 54px;
    text-transform: uppercase; letter-spacing: 1px;
  }
  .front-title .accent {
    color: var(--accent);
    text-decoration: underline; text-decoration-thickness: 3px; text-underline-offset: 4px;
  }
  .front-art {
    position: absolute; left: 615px; top: 186px; width: 190px; height: 255px;
    background: linear-gradient(180deg, var(--art-light), var(--art-mid));
  }
  .front-author {
    position: absolute; left: 540px; top: 522px; width: 320px; text-align: center;
    font-family: "Gochi Hand", cursive; font-size: 19px; letter-spacing: .6px;
    color: var(--paper);
  }
</style>
</head>
<body>
<div class="canvas">
  <section class="spread">
    <svg class="spread-shapes" viewBox="0 0 860 594" preserveAspectRatio="none" aria-hidden="true">
      <path d="M340 594 C470 580 545 410 680 402 C752 398 815 450 860 500 L860 594 Z" fill="#111"/>
    </svg>

    <div class="back-icon" role="img" aria-label="Small scissors illustration"
         style="background: linear-gradient(180deg, var(--art-light), var(--art-mid));"></div>

    <div class="back-copy">
      <p>Millions of people feel the pain, loneliness, and agony of anxiety and depression every day. Many turn to Western medicine in the hopes that a pill will ease the pain and make the problem go away. Oftentimes, this only makes matters worse and doesn’t address the root cause. No one should have to struggle like this when natural answers exist that can address the physical, energetic, emotional, or spiritual causes of anxiety and depression. For 11 long years, Dr. Vance personally struggled with heavy depression until he discovered answers that helped him to completely heal. Walking Out of the Fog is a guide that will help you discover -</p>
      <p class="highlight">The two root physical causes of depression and exactly what to do to start healing today -</p>
      <p class="highlight">How the negative emotions we have stored within from trauma and bad experiences can drive depression -</p>
      <p class="highlight">Tools from Chinese medicine, applied kinesiology, and tapping to help you free your mind and live in peace -</p>
      <p>An actionable plan to help you let go of the pain, suffering, and negative emotions from your past Whether you feel depressed and anxious or know someone who struggles with these issues, Walking Out of the Fog will transform how you think about depression and will give you the tools to heal so that you can be free and live in peace.</p>
    </div>

    <div class="author-photo" role="img" aria-label="Small portrait photo of the author"></div>
    <p class="author-bio">Dr. Vance Holbrook is a board-certified acupuncture physician licensed in the state of Florida. He received his training at the Calder Institute of Holistic Practice. He also graduated with a master’s degree in counseling and psychology from Meadowbrook Seminary of Theology. His mission is to help people transform their health and improve the quality of their life naturally. He lives in Orlando, FL where he runs a holistic medical clinic called Bluepine Wellness Center.</p>
    <p class="author-links">www.drvanceholbrook-example.com<br>Instagram: drvanceholbrook<br>Facebook: bluepinewellnesscenter</p>

    <div class="spine">
      <div class="spine-text">
        <span class="spine-title">WALKING <span class="accent">OUT</span> OF THE FOG</span>
        <span class="spine-author">Dr. Vance Holbrook, AP, MA</span>
      </div>
    </div>

    <h1 class="front-title">Walking <span class="accent">Out</span><br>of the Fog</h1>
    <div class="front-art" role="img" aria-label="Hand-drawn open scissors cutting into the top of a black hill"></div>
    <p class="front-author">Dr. Vance Holbrook, AP, MA</p>
  </section>
</div>
</body>
</html>
```